Commercial Real Estate Executive Recruiting Firm Needs Business Card Design

We need a business card design for BRAMLEY | Executive Recruiting - an executive recruiting firm focused exclusively on the commercial real estate industry. We place professionals ranging from Analyst to the Executive Office covering all investment/finance disciplines (acquisitions, asset management, capital markets, etc.) in all product types (office, retail, multifamily, industrial, land, etc.). We have a passion for helping people (clients and candidates) and have a reputation for being open and honest in our recruiting - and yes, very successful. We have recently developed a new logo and would like to update our business cards as well. I've uploaded some information about our company that contains the new logo.

Target Market(s)

Commercial Real Estate professionals. Primarily in the US. These are typically, smart, driven professionals with finance degrees and MBAs. Primarily men between the ages of 25 and 55.

Industry/Entity Type

Real Estate

Font styles to use
Other font styles liked:
• The font for "BRAMLEY" is Blair ITC (Medium), and "executive recruiting" is Gotham (Book).

Requirements
Must have
• I like the idea of white background on one side and solid color (blue, black, etc.) on back of card.

Would like to utilize the fonts in the logo (to the extent possible) so as to not have too many fonts on card.
Nice to have
• I think the roles (i.e., Acquisitions, Asset Management, etc.,...) is probably likely best placed on the back side of the card with the logo maybe. See attached current business card for content.

```html
<!DOCTYPE html>
<html lang="en">
<head>
<meta charset="utf-8">
<title>BRAMLEY | Executive Recruiting — Business Card</title>
<link rel="stylesheet" href="https://fonts.googleapis.com/css2?family=Questrial&family=Source+Sans+3:wght@400&display=swap">
<style>
  :root {
    --stage: #021b39;
    --brand-blue: #286a98;
    --brand-light: #d3e1ee;
    --ink: #1f1f1f;
    --ink-soft: #5a5a5a;
    --paper: #ffffff;
    --grey-1: #f1f1f2;
    --grey-2: #d9dadc;
  }
  html, body {
    margin: 0;
    width: 1200px;
    height: 900px;
    overflow: hidden;
    background: var(--stage);
  }
  .stage {
    position: relative;
    width: 1200px;
    height: 900px;
  }
  .card {
    position: absolute;
    overflow: hidden;
  }

  /* Back side — solid brand colour */
  .card--back {
    left: 497px;
    top: 55px;
    width: 613px;
    height: 358px;
    background: var(--brand-blue);
  }
  .card--back .wordmark {
    position: absolute;
    left: 0;
    right: 0;
    top: 205px;
    text-align: center;
    color: var(--brand-light);
    font-family: "Questrial", sans-serif;
  }
  .card--back .wordmark__name {
    display: block;
    font-size: 40px;
    letter-spacing: 5px;
    line-height: 1;
  }
  .card--back .wordmark__tag {
    display: block;
    font-size: 18px;
    letter-spacing: 1.5px;
    margin-top: 4px;
  }
  .card--back .website {
    position: absolute;
    left: 0;
    right: 0;
    top: 276px;
    text-align: center;
    color: var(--brand-light);
    font-family: "Source Sans 3", sans-serif;
    font-size: 27px;
  }

  /* Front side — white with contact details */
  .card--front {
    left: 58px;
    top: 449px;
    width: 611px;
    height: 357px;
    background: var(--paper);
  }
  .card--front .edge-band {
    position: absolute;
    left: 0;
    top: 0;
    width: 45px;
    height: 100%;
    background: var(--brand-blue);
  }
  .card--front .backdrop {
    position: absolute;
    left: 45px;
    top: 0;
    right: 0;
    bottom: 0;
    background: linear-gradient(110deg, var(--paper) 0%, var(--grey-1) 45%, var(--grey-2) 100%);
  }
  .card--front .wordmark {
    position: absolute;
    right: 32px;
    top: 34px;
    display: flex;
    align-items: center;
    gap: 12px;
    color: var(--ink);
    font-family: "Questrial", sans-serif;
  }
  .card--front .wordmark__mark {
    width: 34px;
    height: 34px;
    background: var(--brand-blue);
  }
  .card--front .wordmark__text {
    display: flex;
    flex-direction: column;
  }
  .card--front .wordmark__name {
    font-size: 25px;
    letter-spacing: 3px;
    line-height: 1;
  }
  .card--front .wordmark__tag {
    font-size: 12.5px;
    letter-spacing: 1px;
    margin-top: 3px;
  }
  .card--front .contact {
    position: absolute;
    right: 33px;
    top: 224px;
    margin: 0;
    text-align: right;
    color: var(--ink);
    font-family: "Source Sans 3", sans-serif;
    font-style: normal;
    font-size: 18px;
    line-height: 23px;
  }
</style>
</head>
<body>
<main class="stage">
  <section class="card card--back" aria-label="Card back">
    <div class="wordmark">
      <span class="wordmark__name">BRAMLEY</span>
      <span class="wordmark__tag">executive recruiting</span>
    </div>
    <div class="website">www.bramleyrecruiting.com</div>
  </section>

  <section class="card card--front" aria-label="Card front">
    <div class="edge-band"></div>
    <div class="backdrop" role="img" aria-label="Large faint brand decoration in soft greys"></div>
    <div class="wordmark">
      <span class="wordmark__mark"></span>
      <span class="wordmark__text">
        <span class="wordmark__name">BRAMLEY</span>
        <span class="wordmark__tag">executive recruiting</span>
      </span>
    </div>
    <address class="contact">
      2750 Harlow Ridge Drive<br>
      Fairview, Texas 75069<br>
      Phone 214-555-0148<br>
      www.bramleyrecruiting.com
    </address>
  </section>
</main>
</body>
</html>
```